Window Dressing of css files in existing web based application

We have a pretty large application which depends mostly on couple of css file that could be seriously improved. The application generates the pages so this job really consists of updating almost only the css file and possibly defined new css classes and affect them to existing objects, table, div, form etc....

Modifying the html pages structure nor an option OR the goal. The goal truly is to change only css files and possibly classes attribution to existing pages making any change in the css reflects properly in all pages (since they share the same css!!)

Target Market(s)

Veterinary

Coding

Coded - Design and coding required

Number of Pages Required

1 page

Requirements
Must have
• CSS knowledge
Nice to have
• Javascript

```html
<!DOCTYPE html>
<html lang="en">
<head>
<meta charset="utf-8">
<title>Report account – Veterinary Demo Clinic</title>
<link href="https://fonts.googleapis.com/css2?family=Roboto:wght@400;500&display=swap" rel="stylesheet">
<style>
:root{
  --sidebar:#7070c8;
  --sidebar-line:#8c8cd6;
  --page:#f0f0f0;
  --ink:#333338;
  --accent:#8b1c1c;
  --panel-top:#9393de;
  --panel-bottom:#7373cb;
  --card-line:#dcdcdc;
  --footer:#28282e;
  --white:#ffffff;
}
*{box-sizing:border-box;margin:0;padding:0}
html,body{width:1200px;height:1016px;overflow:hidden}
body{position:relative;background:var(--page);font-family:'Roboto',sans-serif;color:var(--ink)}
.topbar{position:absolute;left:0;top:0;width:1200px;height:75px;background:linear-gradient(#fafafa,#e9e9e9);border-bottom:1px solid #d6d6d6}
.brand{position:absolute;left:46px;top:27px;display:flex;align-items:center;gap:8px;font-size:24px;color:var(--accent)}
.brand-dot{width:10px;height:10px;border-radius:50%;background:#4a8fd0}
.topnav{position:absolute;left:589px;top:34px;display:flex;font-size:14px;color:var(--ink)}
.topnav span.sep{margin:0 17px}
.logout{position:absolute;left:1036px;top:0;height:75px;border-left:1px solid #d6d6d6;padding:36px 0 0 16px;font-size:14px;display:flex;gap:7px}
.sidebar{position:absolute;left:0;top:75px;width:276px;height:941px;background:var(--sidebar)}
.sidebar a{display:flex;align-items:center;gap:8px;height:62px;padding-left:80px;color:var(--white);text-decoration:none;font-size:16px;border-bottom:2px solid var(--sidebar-line)}
.sidebar svg{width:15px;height:15px;fill:var(--white)}
.clinic{position:absolute;left:299px;top:112px;font-size:23px;color:#3a3a3a}
.welcome{position:absolute;left:302px;top:152px;font-size:18px;color:var(--accent)}
.panel{position:absolute;left:298px;top:194px;width:852px;height:731px;background:var(--white);box-shadow:0 1px 3px rgba(0,0,0,.15)}
.panel-head{height:62px;background:linear-gradient(var(--panel-top),var(--panel-bottom));color:var(--white);font-size:18px;padding:23px 0 0 28px}
.card{position:absolute;background:var(--white);border:1px solid var(--card-line);box-shadow:0 1px 3px rgba(0,0,0,.12)}
.card-head{height:48px;background:linear-gradient(#fdfdfd,#e7e7e7);border-bottom:1px solid var(--card-line);display:flex;align-items:center;gap:8px;font-size:16px;color:var(--accent)}
.card-head svg{width:16px;height:16px;fill:var(--accent)}
.links{list-style:none;font-size:13px;line-height:21px}
.links li{position:relative;padding-left:14px}
.links li::before{content:"»";position:absolute;left:0;color:var(--accent)}
.panel-foot{position:absolute;top:711px;font-size:11px;color:var(--accent)}
.site-foot{position:absolute;left:276px;top:948px;width:924px;height:68px;background:var(--footer);color:var(--white);font-size:13px}
</style>
</head>
<body>
<header class="topbar">
  <div class="brand"><span>BookWell</span><span class="brand-dot"></span></div>
  <nav class="topnav"><span>My Account</span><span class="sep">|</span><span>Favourites</span><span class="sep">|</span><span>Command List</span><span class="sep">|</span><span>Track List</span></nav>
  <div class="logout">Log out <svg width="18" height="18" viewBox="0 0 18 18"><path d="M8 2h8v14H8" fill="none" stroke="#8b1c1c" stroke-width="2"/><path d="M2 7h6V4l5 5-5 5v-3H2z" fill="#8b1c1c"/></svg></div>
</header>

<nav class="sidebar">
  <a><svg viewBox="0 0 16 16"><path d="M8 1 0 8h2v7h4v-5h4v5h4V8h2z"/></svg>HOME</a>
  <a><svg viewBox="0 0 16 16"><path d="M1 3h8v2H3v8h8V9h2v6H1z"/><path d="M13 1l2 2-7 7H6V8z"/></svg>REVIEWS</a>
  <a><svg viewBox="0 0 16 16"><circle cx="8" cy="5" r="3"/><circle cx="3" cy="6" r="2"/><circle cx="13" cy="6" r="2"/><path d="M2 15c0-4 3-6 6-6s6 2 6 6z"/></svg>CLIENTS</a>
  <a><svg viewBox="0 0 16 16"><circle cx="8" cy="8" r="7"/></svg>CAMPAIGANS</a>
  <a><svg viewBox="0 0 16 16"><path d="M10 2l6 5-6 5V9C6 9 3 10 1 14c0-5 3-8 9-8z"/></svg>REFERA</a>
  <a><svg viewBox="0 0 16 16"><path d="M0 3h16v2L8 10 0 5zM0 7l8 5 8-5v7H0z"/></svg>OUT BOX</a>
  <a><svg viewBox="0 0 16 16"><path d="M5 1h7v10H5zM2 5h2v8h7v2H2z"/></svg>REPORT</a>
</nav>

<h1 class="clinic" style="font-weight:400">The Veterinary Demo Clinic #2588</h1>
<p class="welcome">Welcome to your Report account</p>

<main class="panel">
  <div class="panel-head">WHAT DO YOU WANT TO DO?</div>

  <section class="card" style="left:32px;top:85px;width:508px;height:238px">
    <div class="card-head" style="padding-left:40px"><svg viewBox="0 0 16 16"><path d="M14 2a4 4 0 0 0-5 5L1 13l2 2 6-8a4 4 0 0 0 5-5l-2 2-2-2z"/></svg>SETUP</div>
    <ul class="links" style="position:absolute;left:41px;top:80px;display:grid;row-gap:17px"><li>Account information</li><li>Office hours</li><li>Online scheduling parameters</li><li>Client communications</li></ul>
    <ul class="links" style="position:absolute;left:272px;top:76px;display:grid;row-gap:17px"><li>Email templates</li><li>Online scheduling website layout</li><li>Health Certificates</li></ul>
  </section>

  <section class="card" style="left:560px;top:85px;width:271px;height:238px">
    <div class="card-head" style="padding-left:32px"><svg viewBox="0 0 16 16"><path d="M1 3h14v12H1zm2 4v6h10V7z"/><path d="M4 1h2v4H4zm6 0h2v4h-2z"/></svg>SCHDULE</div>
    <ul class="links" style="position:absolute;left:36px;top:80px;width:226px;display:grid;row-gap:15px"><li>View your appointment calender by column or by provider</li><li>Clients</li></ul>
  </section>

  <section class="card" style="left:35px;top:334px;width:258px;height:206px">
    <div class="card-head" style="padding-left:33px"><svg viewBox="0 0 16 16"><path d="M1 3h14v12H1zm2 4v6h10V7z"/></svg>CAMPAIGNS</div>
    <ul class="links" style="position:absolute;left:21px;top:66px;width:230px;display:grid;row-gap:17px"><li>Use the Media Center to: Send vaccine reminders through</li><li>Email, text, phone, or postcard Send marketing communications</li></ul>
  </section>

  <section class="card" style="left:301px;top:334px;width:258px;height:206px">
    <div class="card-head" style="padding-left:30px"><svg viewBox="0 0 16 16"><circle cx="8" cy="5" r="3"/><circle cx="3" cy="6" r="2"/><circle cx="13" cy="6" r="2"/><path d="M2 15c0-4 3-6 6-6s6 2 6 6z"/></svg>CLIENTS</div>
    <ul class="links" style="position:absolute;left:28px;top:64px;width:226px;display:grid;row-gap:17px"><li>View client and patient records</li><li>View opt-out reports</li><li>View client appointment &amp; communication history</li></ul>
  </section>

  <section class="card" style="left:568px;top:334px;width:258px;height:206px">
    <div class="card-head" style="padding-left:36px"><svg viewBox="0 0 16 16"><path d="M0 3h16v2L8 10 0 5zM0 7l8 5 8-5v7H0z"/></svg>OUTBOX</div>
    <ul class="links" style="position:absolute;left:20px;top:65px;width:232px;display:grid;row-gap:17px"><li>View the account’s communication history</li><li>Access the archives for any messages previously sent</li></ul>
  </section>

  <section class="card" style="left:35px;top:552px;width:791px;height:137px">
    <div class="card-head" style="padding-left:29px"><svg viewBox="0 0 16 16"><ellipse cx="6" cy="7" rx="6" ry="5"/><ellipse cx="11" cy="10" rx="5" ry="4"/></svg>REVIEWS</div>
    <ul class="links" style="position:absolute;left:36px;top:84px"><li>View Surveys results and monitor any recent Surveys activity</li></ul>
  </section>

  <p class="panel-foot" style="left:42px">Today is 4/412015</p>
  <p class="panel-foot" style="right:30px">Confirmation list&nbsp; I&nbsp; Task List</p>
</main>

<footer class="site-foot">
  <p style="position:absolute;left:25px;top:26px">Copyright © 2015&nbsp; All Rights Reserved</p>
  <p style="position:absolute;right:23px;top:29px;font-size:12px">C6</p>
</footer>
</body>
</html>
```